Looking for a Lumora Book Cover

My book has been online for a while and I am now looking for a professional cover for it as it has been very well received.

You can view the book here and all the details about it:

https://www.pagevaultshop.example/dp/X7Q2KRMTPL#readerNotes

Not sure what I am looking for as a design, just open to your ideas.

I want something different that will stand out please.

Thanks
Owen

```html
<!DOCTYPE html>
<html lang="en">
<head>
<meta charset="UTF-8">
<title>Roots and Resillience — Book Cover</title>
<link rel="stylesheet" href="https://fonts.googleapis.com/css2?family=Jost:wght@500;600&family=Antonio:wght@700&display=swap">
<style>
  :root {
    --page-bg: #e9e9e9;
    --cover-black: #141414;
    --ink-white: #f4f1ea;
    --title-orange: #f07a1c;
    --title-amber: #f4a21a;
    --title-yellow: #f2c81c;
  }
  * { margin: 0; padding: 0; box-sizing: border-box; }
  html, body {
    width: 1200px;
    height: 900px;
    overflow: hidden;
    background: var(--page-bg);
  }
  .book-cover {
    position: absolute;
    left: 394px;
    top: 95px;
    width: 450px;
    height: 705px;
    background: var(--cover-black);
    color: var(--ink-white);
    font-family: "Jost", sans-serif;
    text-align: center;
  }
  .author-name {
    position: absolute;
    top: 18px;
    left: 0;
    width: 100%;
    font-size: 22px;
    line-height: 30px;
    font-weight: 500;
    letter-spacing: 0.24em;
    padding-left: 0.24em;
  }
  .portrait-area {
    position: absolute;
    left: 70px;
    top: 70px;
    width: 240px;
    height: 240px;
    background: radial-gradient(ellipse at 45% 45%, #333 0%, #222 30%, var(--cover-black) 68%);
  }
  .subtitle {
    position: absolute;
    top: 321px;
    left: 0;
    width: 100%;
    font-size: 14px;
    font-weight: 600;
    line-height: 19.5px;
    letter-spacing: 0.2em;
    padding-left: 0.2em;
  }
  .main-title {
    position: absolute;
    top: 393px;
    left: 0;
    width: 450px;
    height: 236px;
    overflow: visible;
  }
  .main-title text {
    font-family: "Antonio", sans-serif;
    font-weight: 700;
    font-size: 126px;
  }
  .tagline {
    position: absolute;
    top: 637px;
    left: 0;
    width: 100%;
    font-size: 16px;
    font-weight: 600;
    line-height: 22px;
    letter-spacing: 0.2em;
    padding-left: 0.2em;
  }
  .tagline .accent-amber { color: var(--title-amber); }
  .tagline .accent-orange { color: var(--title-orange); }
  .tagline .accent-yellow { color: var(--title-yellow); }
</style>
</head>
<body>
  <main class="book-cover">
    <p class="author-name">DESMOND ASHCOMBE</p>

    <div class="portrait-area" role="img" aria-label="Dramatic low-key portrait photograph of a man's face emerging from darkness"></div>

    <p class="subtitle">The History, Resistance<br>and Excellence of Black People<br>in Africa and the Diaspora</p>

    <svg class="main-title" viewBox="0 0 450 236" aria-label="Roots and Resillience">
      <defs>
        <linearGradient id="titleGradient" x1="70" y1="0" x2="381" y2="0" gradientUnits="userSpaceOnUse">
          <stop offset="0" stop-color="var(--title-orange)"/>
          <stop offset="0.5" stop-color="var(--title-yellow)"/>
          <stop offset="1" stop-color="var(--title-orange)"/>
        </linearGradient>
      </defs>
      <text x="77" y="110" textLength="296" lengthAdjust="spacingAndGlyphs" fill="url(#titleGradient)">ROOTS AND</text>
      <text x="71" y="232" textLength="309" lengthAdjust="spacingAndGlyphs" fill="url(#titleGradient)">RESILLIENCE</text>
    </svg>

    <p class="tagline">A CELEBRATION OF <span class="accent-amber">CULTURE,</span><br><span class="accent-orange">STRUGGLE</span> AND <span class="accent-yellow">ACHIEVEMENT</span></p>
  </main>
</body>
</html>
```